Supplement Label and Logo design

We are creating a premium brand nootropics (to improve brain function) supplement and would like a label with a logo designed.
Name: Tallowfen Nootropics
Tag Line: The higher power premium nootropics supplement
Include three bullet points:
Can contribute to:
-Improved Focus, Memory & Mood
-Stress & Anxiety Reduction
-Immune System Support
State on label:-
-Made in the UK and include Union Jack logo
-Vegan
Label Design:
A Tallowfen Nootropics logo
We would like a combination of blue and white colours on the label itself with a gold trim at the top and bottom of the label.
We may need some revisions to the content on the label.
We will need to include a supplement facts section. An example of this is attached.

```html
<!DOCTYPE html>
<html lang="en">
<head>
<meta charset="utf-8">
<title>Tallowfen Nootropics – Supplement Label</title>
<link rel="stylesheet" href="https://fonts.googleapis.com/css2?family=Exo+2:wght@700&family=Barlow:wght@300;400;600;700&family=Playfair+Display:wght@800&display=swap">
<style>
  :root {
    --navy: #0b1760;
    --navy-deep: #050d45;
    --navy-soft: #dfe2ef;
    --gold-light: #d9822b;
    --gold: #b8651a;
    --gold-dark: #7a3f0e;
    --white: #ffffff;
    --label-bg: #f4f5f6;
    --page-bg: #e6e7e9;
  }
  * { box-sizing: border-box; margin: 0; padding: 0; }
  html, body {
    width: 1200px; height: 1200px; overflow: hidden;
    background: var(--page-bg);
    font-family: "Barlow", Arial, sans-serif;
  }
  .label {
    position: absolute; left: 100px; top: 77px;
    width: 1000px; height: 1046px;
    background: var(--label-bg);
    overflow: hidden;
  }
  .header-band { position: absolute; left: 0; top: 0; width: 1000px; height: 440px; }
  .brand {
    position: absolute; left: 0; top: 40px; width: 1000px;
    display: flex; flex-direction: column; align-items: center;
  }
  .brand-name {
    display: flex; align-items: center; gap: 22px;
    font-family: "Exo 2", Arial, sans-serif; font-weight: 700;
    color: var(--white); font-size: 84px; line-height: 1; letter-spacing: 1px;
  }
  .brand-mark {
    width: 54px; height: 54px; border-radius: 50%;
    border: 5px solid var(--white); flex: none;
  }
  .brand-line { font-size: 74px; text-align: center; }
  .tagline {
    margin-top: 18px; padding: 5px 4px;
    border-top: 2px solid var(--white); border-bottom: 2px solid var(--white);
    color: var(--white); font-weight: 600; font-size: 20px; letter-spacing: 0.3px;
  }
  .hero-icon {
    position: absolute; left: 340px; top: 470px; width: 320px; height: 330px;
    border-radius: 48% 48% 44% 44%;
    background: radial-gradient(circle, var(--navy-soft) 0%, #eceef4 70%, var(--label-bg) 100%);
  }
  .vegan {
    position: absolute; left: 100px; top: 790px; color: var(--navy);
  }
  .vegan-pct { font-weight: 700; font-size: 26px; line-height: 1; }
  .vegan-word {
    font-family: "Playfair Display", Georgia, serif; font-weight: 800;
    font-size: 58px; line-height: 0.9; letter-spacing: -1px;
  }
  .count {
    position: absolute; right: 108px; top: 780px; text-align: center; color: var(--navy);
  }
  .count-num { font-weight: 700; font-size: 62px; line-height: 1; letter-spacing: 3px; }
  .count-unit { font-weight: 700; font-size: 19px; letter-spacing: 0.5px; }
  .benefits {
    position: absolute; left: 60px; top: 883px; width: 882px; height: 130px;
    border: 2px solid var(--navy); border-bottom: none; border-radius: 12px 12px 0 0;
    display: flex; align-items: center; justify-content: space-around; padding: 24px 10px 0;
  }
  .benefits-title {
    position: absolute; top: -16px; left: 50%; transform: translateX(-50%);
    background: var(--label-bg); padding: 0 6px;
    color: var(--navy); font-weight: 700; font-size: 25px; letter-spacing: 0.5px; white-space: nowrap;
  }
  .benefit { display: flex; align-items: center; gap: 14px; }
  .benefit + .benefit { border-left: 3px solid var(--navy); padding-left: 26px; }
  .benefit-icon {
    width: 62px; height: 62px; border-radius: 50%; background: var(--navy-soft); flex: none;
  }
  .benefit-icon.solid { background: var(--navy); opacity: 0.85; }
  .benefit-text { color: var(--navy); font-weight: 300; font-size: 24px; line-height: 1.1; }
  .footer-band {
    position: absolute; left: 0; bottom: 0; width: 1000px; height: 56px;
    background: linear-gradient(90deg, var(--gold-dark), var(--gold) 18%, var(--gold-light) 50%, var(--gold) 82%, var(--gold-dark));
    border-top: 3px solid var(--gold-dark);
    display: flex; align-items: center; justify-content: center;
    color: var(--white); font-weight: 600; font-size: 34px; letter-spacing: 3px;
  }
</style>
</head>
<body>
<main class="label">
  <svg class="header-band" viewBox="0 0 1000 440" aria-hidden="true">
    <defs>
      <linearGradient id="gold-trim" x1="0" x2="1" y1="0" y2="0">
        <stop offset="0" stop-color="#7a3f0e"/>
        <stop offset="0.5" stop-color="#d9822b"/>
        <stop offset="1" stop-color="#7a3f0e"/>
      </linearGradient>
      <linearGradient id="navy-fill" x1="0" x2="1" y1="0" y2="0">
        <stop offset="0" stop-color="#0b1760"/>
        <stop offset="0.5" stop-color="#050d45"/>
        <stop offset="1" stop-color="#0b1760"/>
      </linearGradient>
    </defs>
    <rect x="0" y="0" width="1000" height="10" fill="url(#gold-trim)"/>
    <polygon points="0,255 500,405 1000,255 1000,278 500,428 0,278" fill="url(#gold-trim)"/>
    <polygon points="0,10 1000,10 1000,258 500,408 0,258" fill="url(#navy-fill)"/>
  </svg>

  <header class="brand">
    <div class="brand-name">
      <span class="brand-mark"></span>
      <div>
        <div class="brand-line">Tallowfen</div>
        <div class="brand-line">Nootropics</div>
      </div>
    </div>
    <p class="tagline">The Higher Power Premium Nootropic &amp; Adaptogen Supplement</p>
  </header>

  <div class="hero-icon" role="img" aria-label="Line icon of a brain with radiating rays"></div>

  <div class="vegan">
    <div class="vegan-pct">100%</div>
    <div class="vegan-word">vegan</div>
  </div>

  <div class="count">
    <div class="count-num">120</div>
    <div class="count-unit">CAPSULES</div>
  </div>

  <section class="benefits">
    <h2 class="benefits-title">CAN CONTRIBUTE TO</h2>
    <div class="benefit">
      <div class="benefit-icon" role="img" aria-label="Brain icon with plus sign"></div>
      <p class="benefit-text">Improved Focus,<br>Memory &amp; Mood</p>
    </div>
    <div class="benefit">
      <div class="benefit-icon solid" role="img" aria-label="Icon of a stressed figure with downward arrow"></div>
      <p class="benefit-text">Stress &amp; Anxiety<br>Reduction</p>
    </div>
    <div class="benefit">
      <svg width="58" height="62" viewBox="0 0 58 62" aria-hidden="true">
        <path d="M29 3 L53 11 V30 C53 45 42 54 29 59 C16 54 5 45 5 30 V11 Z" fill="none" stroke="#0b1760" stroke-width="3"/>
        <path d="M29 10 L47 16 V30 C47 41 39 48 29 52 C19 48 11 41 11 30 V16 Z" fill="none" stroke="#0b1760" stroke-width="2"/>
        <path d="M25 21 H33 V27 H39 V35 H33 V41 H25 V35 H19 V27 H25 Z" fill="none" stroke="#0b1760" stroke-width="2.5"/>
      </svg>
      <p class="benefit-text">Immune System<br>Support</p>
    </div>
  </section>

  <footer class="footer-band">FOOD SUPPLEMENT</footer>
</main>
</body>
</html>
```